Brightpath Wellness Referral Program

We have recently started a referral program for our clinics and we need a postcard that we can hand our to clients to let them know about the new program.
We are looking for a 4x6" card design that highlights our incentive referral program while visually either showing some of the services we offer, or, conveying a message of health, community, family, etc.
The details of our referral program can be found at:
https://brightpathwellness.ca/about/refer-a-friend.html
We would also like to see somewhere on the card, 2 lines for:
1) Your name: ( new clients name)
2) Referred by: __________
The card can be single or double sided, whatever looks best for design purposes.
Target Market(s)
Ages 20-50, equal men and women
Look and feel
Each slider illustrates characteristics of the customer's brand and the style your logo design should communicate.

```html
<!DOCTYPE html>
<html lang="en">
<head>
<meta charset="utf-8">
<title>Brightpath Wellness Referral Postcard</title>
<link href="https://fonts.googleapis.com/css2?family=Roboto:ital,wght@0,400;0,700;1,400;1,500&family=Roboto+Condensed:wght@700&family=Montserrat:wght@800;900&display=swap" rel="stylesheet">
<style>
  :root {
    --navy: #1d3a63;
    --blue: #0f6ab3;
    --blue-soft: #5c93c8;
    --orange: #f26b0f;
    --grey: #a7a9ab;
    --ink: #1f2328;
    --white: #ffffff;
    --backdrop: #e9e6e1;
  }
  * { margin: 0; padding: 0; box-sizing: border-box; }
  html, body { width: 1200px; height: 923px; overflow: hidden; }
  body {
    background: var(--backdrop);
    font-family: "Roboto", Arial, sans-serif;
    position: relative;
  }
  .card {
    position: absolute;
    width: 590px;
    height: 393px;
    overflow: hidden;
    background: var(--white);
    box-shadow: 0 6px 18px rgba(0,0,0,.18);
  }
  .card svg.shapes { position: absolute; inset: 0; }

  /* ---------- Front ---------- */
  .card--front { left: 40px; top: 40px; }
  .brand {
    position: absolute;
    display: flex;
    align-items: center;
    gap: 7px;
    font-family: "Roboto", Arial, sans-serif;
    font-weight: 700;
    white-space: nowrap;
  }
  .brand__dot { border-radius: 50%; display: block; }
  .card--front .brand { left: 30px; top: 38px; font-size: 21px; color: var(--white); }
  .card--front .brand__dot { width: 20px; height: 20px; background: var(--white); }

  .form-field { position: absolute; left: 46px; width: 235px; color: var(--ink); }
  .form-field__label { font-weight: 700; font-size: 13px; }
  .form-field__line { border-bottom: 1.5px dotted var(--ink); height: 14px; }
  .form-field__hint { font-style: italic; font-size: 6.5px; text-align: center; margin-top: 3px; }
  .form-field--name { top: 268px; }
  .form-field--referrer { top: 320px; }

  /* ---------- Back ---------- */
  .card--back { left: 570px; top: 490px; }
  .kicker {
    position: absolute; left: 0; top: 19px;
    width: 267px; height: 22px;
    background: var(--white);
    border-radius: 0 11px 11px 0;
    font-family: "Roboto Condensed", Arial Narrow, sans-serif;
    font-weight: 700; font-size: 12.5px; color: var(--orange);
    line-height: 22px; padding-left: 20px;
  }
  .headline {
    position: absolute; left: 19px; top: 40px;
    font-family: "Roboto Condensed", Arial Narrow, sans-serif;
    font-weight: 700; font-size: 41px; color: var(--white);
    letter-spacing: -.3px; white-space: nowrap;
  }
  .intro { position: absolute; left: 20px; top: 90px; width: 320px; color: var(--white); font-size: 10.4px; line-height: 13px; }
  .intro p + p { margin-top: 7px; }
  .intro b, .details b { font-weight: 700; }

  .reward { position: absolute; left: 20px; display: flex; align-items: center; }
  .reward__arrow { width: 0; height: 0; border-left: 8px solid var(--orange); border-top: 5px solid transparent; border-bottom: 5px solid transparent; margin-right: 14px; }
  .reward__amount { width: 55px; font-family: "Montserrat", Arial, sans-serif; font-weight: 900; line-height: .9; text-align: right; }
  .reward__earn { display: block; color: var(--blue); font-size: 11px; font-weight: 800; }
  .reward__value { display: block; color: var(--orange); font-size: 25px; }
  .reward__text { margin-left: 9px; width: 240px; font-weight: 700; font-size: 10.2px; line-height: 13px; color: var(--ink); }
  .reward--south { top: 196px; }
  .reward--north { top: 236px; }

  .details { position: absolute; left: 20px; top: 274px; width: 385px; font-size: 10.3px; line-height: 13px; color: var(--ink); }
  .fineprint { position: absolute; left: 20px; top: 338px; width: 408px; font-size: 5.5px; line-height: 8.2px; font-style: italic; color: var(--ink); text-align: justify; }

  .slogan {
    position: absolute; right: 0; top: 76px;
    font-family: "Montserrat", Arial, sans-serif; font-weight: 900;
    font-size: 40px; line-height: 31px; letter-spacing: -1.2px;
    color: var(--white); text-align: right;
  }
  .slogan__accent { color: var(--ink); }

  .badge {
    position: absolute; width: 94px; height: 60px; border-radius: 50%;
    background: var(--white); border: 3px solid var(--orange);
    font-family: "Montserrat", Arial, sans-serif; font-weight: 900; color: var(--orange);
    text-align: center; line-height: 1;
  }
  .badge__earn { display: block; font-size: 10px; margin-top: 6px; }
  .badge__value { display: block; font-size: 31px; letter-spacing: -1px; }
  .badge--25 { left: 398px; top: 8px; }
  .badge--10 { left: 465px; top: 271px; }

  .card--back .brand { left: 444px; top: 354px; font-size: 12.5px; color: var(--blue); }
  .card--back .brand__dot { width: 14px; height: 14px; background: var(--grey); }
</style>
</head>
<body>

<section class="card card--front">
  <svg class="shapes" viewBox="0 0 590 393" width="590" height="393">
    <defs>
      <linearGradient id="front-fade" x1="0" y1="0" x2="0" y2="1">
        <stop offset="0" stop-color="#0f6ab3"/>
        <stop offset=".55" stop-color="#2f72b0"/>
        <stop offset=".8" stop-color="#9cc0e2"/>
        <stop offset="1" stop-color="#ffffff"/>
      </linearGradient>
      <linearGradient id="portrait-tone" x1="0" y1="0" x2="1" y2="1">
        <stop offset="0" stop-color="#dfe3e6"/>
        <stop offset=".6" stop-color="#c9d6e4"/>
        <stop offset="1" stop-color="#a9c3df"/>
      </linearGradient>
    </defs>
    <rect width="590" height="393" fill="url(#front-fade)" role="img" aria-label="Blue-toned photo of a client relaxing during a back massage"/>
    <ellipse cx="470" cy="190" rx="235" ry="250" fill="#f4f4f4"/>
    <ellipse cx="505" cy="190" rx="215" ry="240" fill="url(#portrait-tone)" role="img" aria-label="Photo of a surprised woman holding a fan of banknotes and pointing at them"/>
  </svg>

  <div class="brand"><span class="brand__dot"></span>Brightpath Wellness</div>

  <div class="form-field form-field--name">
    <div class="form-field__label">Name:</div>
    <div class="form-field__line"></div>
    <div class="form-field__hint">(new clients name)</div>
  </div>
  <div class="form-field form-field--referrer">
    <div class="form-field__label">Referred by:</div>
    <div class="form-field__line"></div>
  </div>
</section>

<section class="card card--back">
  <svg class="shapes" viewBox="0 0 590 393" width="590" height="393">
    <defs>
      <linearGradient id="header-navy" x1="0" y1="0" x2="1" y2="0">
        <stop offset="0" stop-color="#1d3a63"/>
        <stop offset="1" stop-color="#1a5796"/>
      </linearGradient>
    </defs>
    <path d="M0 0 H500 C430 40 372 100 356 158 C250 186 120 186 0 160 Z" fill="url(#header-navy)"/>
    <path d="M500 0 H590 V345 C500 332 362 282 348 176 C342 100 420 30 500 0 Z" fill="var(--grey)"/>
    <path d="M540 0 H590 V342 C520 336 398 282 386 176 C380 100 450 30 540 0 Z" fill="var(--blue)"/>
    <rect x="0" y="388" width="590" height="5" fill="var(--orange)"/>
  </svg>

  <div class="kicker">ANNOUNCING OUR NEWLY REDESIGNED</div>
  <h1 class="headline">REFERRAL PROGRAM</h1>

  <div class="intro">
    <p>Referrals are the <b>lifeblood</b> of our small business.</p>
    <p>We are <b>incredibly grateful</b> for your trust and recommendations over the years, and we want to show our gratitude. That's why we are introducing an exciting new way to earn more free treatment. Now you can:</p>
  </div>

  <div class="reward reward--south">
    <span class="reward__arrow"></span>
    <span class="reward__amount"><span class="reward__earn">Earn</span><span class="reward__value">$25</span></span>
    <span class="reward__text">for every referral you make to our south Calgary location (Ridgeview Drive), and;</span>
  </div>
  <div class="reward reward--north">
    <span class="reward__arrow"></span>
    <span class="reward__amount"><span class="reward__earn">Earn</span><span class="reward__value">$10</span></span>
    <span class="reward__text">for every referral you make to our north Calgary location(Maplecrest).</span>
  </div>

  <p class="details">Credits can be <b>used for any service at either our north or south location</b> and, in the spirit of community, <b>credits are transferable</b>. Refer 4 people to the south and you could gift someone a $100 gift card! Or, enjoy a well deserved, free treatment yourself.</p>

  <p class="fineprint">*Referral(s) must be brand new client(s) to the Brightpath Wellness Inc. practice, having never booked or attended an appointment at any Brightpath Wellness location. Referral must attend their appointment for you to be eligible for a referral credit. Referral credit value is dependent upon which Brightpath Wellness location your referral attends: you are eligible for a $10 credit for a referral to our north location (#410 - 1880 Maplecrest Parkway NW); you are eligible for a $25 credit for a referral to our south location (#120 - 6400 Ridgeview Drive SE). We are really good at asking but please remind your referral to tell us it is YOU who we have to thank! Credit(s) may be redeemed as payment or partial payment for any service at any Brightpath Wellness location. Credits have no cash value and no expiry.</p>

  <div class="slogan">GOOD<br>PEOPLE<br><span class="slogan__accent">KNOW</span><br>GOOD<br>PEOPLE</div>

  <div class="badge badge--25"><span class="badge__earn">Earn</span><span class="badge__value">$25</span></div>
  <div class="badge badge--10"><span class="badge__earn">Earn</span><span class="badge__value">$10</span></div>

  <div class="brand"><span class="brand__dot"></span>Brightpath Wellness</div>
</section>

</body>
</html>
```